Robotic startup business cards

We are looking for a design for a set of business cards which reflect the spirit and humor of Vortalo Robotics. We want to present ourselves as sleek, professional, but laid-back consulting company.

We primarily focus on developing robotic arms software. This software controls robots and does things like grab items, pick objects up, move them, etc.

We want to allow you maximum design creativity, but do ask that you consider our existing style guidelines (see attached files) in order to make our brand cohesive.

Target Market(s)

Startups and Mid-size robotic companies

Industry/Entity Type

Business

Contact Information for Business Card

Miro Halvensky, PhD
Roboticist | Vortalo Consulting | 318.570.9164

Font styles to use
Other font styles liked:
• Source code pro

Requirements
Must have
• robots or robotic arms
• similar color scheme that works with existing brand guidelines
Nice to have
• please consider our existing style guidelines (see attached files) in order to make our brand cohesive.
• minimalism style is generally nice.
Should not have
• An old, boring, or corporate feel. Too much text.

```html
<!DOCTYPE html>
<html lang="en">
<head>
<meta charset="utf-8">
<title>Vortalo Consulting business cards</title>
<link rel="stylesheet" href="https://fonts.googleapis.com/css2?family=Source+Code+Pro:wght@400;600;700&display=swap">
<style>
  :root {
    --page: #ffffff;
    --ink: #111111;
    --band: #141414;
    --accent: #1fe06a;
    --brand-green: #3cb54a;
    --glow: #f2fbf2;
    --steel-light: #ffffff;
    --steel-dark: #7f7f7f;
  }
  html, body {
    margin: 0;
    padding: 0;
    width: 1199px;
    height: 1200px;
    overflow: hidden;
    background: var(--page);
  }
  .sheet {
    position: relative;
    width: 1199px;
    height: 1200px;
  }
  .card {
    position: absolute;
    left: 201px;
    width: 797px;
    height: 452px;
    overflow: hidden;
    box-shadow: 0 18px 22px -10px rgba(0,0,0,0.55);
  }
  /* Front card */
  .card--front {
    top: 112px;
    background: var(--page);
    border: 1px solid #333;
    box-sizing: border-box;
  }
  .front__band {
    position: absolute;
    left: 0; top: 38px;
    width: 100%; height: 52px;
    background: var(--band);
  }
  .front__name {
    position: absolute;
    left: 39px; top: 47px;
    margin: 0;
    font-family: "Verdana", "DejaVu Sans", sans-serif;
    font-weight: 700;
    font-size: 32px;
    letter-spacing: 4px;
    word-spacing: 10px;
    line-height: 1;
    color: var(--accent);
  }
  .front__body {
    position: absolute;
    left: 0; top: 96px;
    width: 100%; height: 356px;
    background: linear-gradient(90deg, var(--steel-light) 0%, #c8c8c8 35%, #a4a4a4 60%, var(--steel-dark) 100%);
  }
  .front__robot {
    position: absolute;
    left: 3px; top: 200px;
    width: 234px; height: 252px;
    background: linear-gradient(180deg, #9a9a9a 0%, #6f6f6f 100%);
    opacity: 0.55;
  }
  .front__details {
    position: absolute;
    left: 264px; top: 278px;
    margin: 0;
    font-family: "Source Code Pro", monospace;
    font-weight: 700;
    font-size: 42px;
    line-height: 58px;
    color: var(--ink);
    white-space: nowrap;
  }
  /* Back card */
  .card--back {
    top: 658px;
    height: 456px;
    background: radial-gradient(ellipse 420px 330px at 391px 286px, var(--glow) 0%, #9fdca2 30%, #62c46a 60%, var(--brand-green) 100%);
  }
  .back__brand {
    position: absolute;
    left: 0; top: 175px;
    width: 100%;
    margin: 0;
    text-align: center;
    font-family: "Source Code Pro", monospace;
    font-weight: 400;
    font-size: 80px;
    letter-spacing: 2px;
    line-height: 1;
    color: var(--ink);
  }
  .back__band {
    position: absolute;
    left: 0; bottom: 0;
    width: 100%; height: 78px;
    background: var(--band);
    text-align: center;
    font-family: "Source Code Pro", monospace;
    font-weight: 700;
    font-size: 26px;
    line-height: 30px;
    padding-top: 9px;
    box-sizing: border-box;
  }
  .back__name { color: var(--accent); margin: 0; }
  .back__meta { color: #ffffff; margin: 0; white-space: nowrap; }
</style>
</head>
<body>
<main class="sheet">
  <section class="card card--front">
    <div class="front__band"></div>
    <h1 class="front__name">MIRO HALVENSKY, PHD</h1>
    <div class="front__body"></div>
    <div class="front__robot" role="img" aria-label="Illustration of a grey industrial robotic arm with a gripper on a pedestal"></div>
    <p class="front__details">ROBOTICIST<br>VORTALO CONSULTING<br>318 570 9164</p>
  </section>

  <section class="card card--back">
    <p class="back__brand">VORTALO</p>
    <div class="back__band">
      <p class="back__name">MIRO HALVENSKY, PHD</p>
      <p class="back__meta">ROBOTICIST | VORTALO CONSULTING | 318 570 9164</p>
    </div>
  </section>
</main>
</body>
</html>
```